TFP Tarlo Fluid Power company brochure

We need the design of brochure of a company that provides consultancy, design and supply of key equipment in the field of Wastewater, clean water, organic waste anaerobic treatment and green energy production for Industries. The attached files are:
TFP wording in english that describes activities
Some drawings (useful for design)
Presentation (in italian)
It would be nice to have a 4 pages brochure possibly in double language (english and italian).

Target Market(s)

water and waste

Industry/Entity Type

It Company

Colors

Designer to choose colors to be used in the design.

Requirements
Must have
• use the logo TFP as per attached docs

```html
<!DOCTYPE html>
<html lang="en">
<head>
<meta charset="utf-8">
<title>TFP Tarlo Fluid Power – Brochure Spread</title>
<link rel="stylesheet" href="https://fonts.googleapis.com/css2?family=Arimo:wght@400;700&display=swap">
<style>
  :root {
    --page: #ffffff;
    --ink: #3a3a3a;
    --green: #4f9a12;
    --blue: #1d5c97;
    --brand: #2f7d32;
    --lab-a: #b9c0c4;
    --lab-b: #6f7a80;
    --tank-a: #c9b98a;
    --tank-b: #8e8a6c;
    --sludge-a: #c4a98c;
    --sludge-b: #8f7d6a;
    --steel-a: #c9cdd0;
    --steel-b: #7d8589;
  }
  * { box-sizing: border-box; margin: 0; padding: 0; }
  html, body { width: 1200px; height: 481px; overflow: hidden; background: var(--page); }
  body { font-family: "Arimo", Arial, sans-serif; color: var(--ink); }

  .spread { position: relative; width: 1200px; height: 481px; display: flex; }
  .page { position: relative; width: 600px; height: 481px; background: var(--page); }
  .page--left { background: linear-gradient(to right, #fff 88%, #ececec 100%); }
  .page--right { background: linear-gradient(to right, #e6e6e6 0%, #fff 8%); }

  .brand {
    position: absolute;
    display: flex; align-items: center; gap: 6px;
    font-weight: 700; font-size: 14px; line-height: 1; color: var(--brand);
  }
  .brand__dot { width: 12px; height: 12px; border-radius: 50%; background: var(--brand); }
  .page--left .brand { left: 26px; top: 32px; }
  .page--right .brand { right: 24px; bottom: 26px; }

  .photo { position: absolute; display: block; }
  .photo--lab { left: 0; top: 128px; width: 290px; height: 222px;
    background: linear-gradient(135deg, var(--lab-a), var(--lab-b)); }

  .mission { position: absolute; left: 340px; top: 128px; width: 250px; }
  .mission__title { font-size: 26px; font-weight: 400; color: var(--green); margin-left: 30px; letter-spacing: .2px; }
  .mission__title b { font-weight: 700; }
  .mission__cols { display: flex; gap: 14px; margin-top: 14px; font-size: 8.6px; line-height: 1.25; }
  .mission__col { width: 118px; }
  .mission__col p { margin-bottom: 10px; }
  .mission__col--en p { position: relative; padding-left: 8px; }
  .mission__col--en p::before { content: "•"; position: absolute; left: 0; }

  .provide { position: absolute; left: 20px; top: 118px; width: 252px; }
  .provide__title { font-size: 31px; font-weight: 400; color: var(--blue); margin-left: 14px; }
  .provide__title b { font-weight: 700; }
  .provide__list { list-style: none; margin-top: 16px; font-size: 11px; line-height: 1.28; }
  .provide__list li { position: relative; padding-left: 16px; margin-bottom: 10px; white-space: nowrap; }
  .provide__list li::before { content: "•"; position: absolute; left: 2px; }

  .gallery { position: absolute; left: 280px; top: 134px; width: 296px; display: flex; flex-direction: column; gap: 3px; }
  .gallery .photo { position: static; width: 100%; }
  .photo--tank { height: 58px; background: linear-gradient(160deg, var(--tank-a), var(--tank-b)); }
  .photo--basin { height: 60px; background: linear-gradient(160deg, var(--sludge-a), var(--sludge-b)); }
  .photo--screw { height: 58px; background: linear-gradient(160deg, #d2b89c, #9c8470); }
  .photo--plant { height: 56px; background: linear-gradient(160deg, var(--steel-a), var(--steel-b)); }
</style>
</head>
<body>
<main class="spread">
  <section class="page page--left">
    <div class="brand"><span class="brand__dot"></span>TFP Tarlo Fluid Power</div>

    <div class="photo photo--lab" role="img" aria-label="Photo of a technician in a white coat working at a laboratory bench with glassware"></div>

    <article class="mission">
      <h2 class="mission__title">Our <b>Mission</b></h2>
      <div class="mission__cols">
        <div class="mission__col mission__col--en">
          <p><b>TFP ltd (TFP)</b> has the mission to solve any client's environmental problem with best process solution available on the market, most reliable and economical both on the CAPEX and OPEX.</p>
          <p><b>TFP</b> want to optimize the client's benefits : energy, water recycle, products recovery and emission minimization.</p>
          <p><b>TFP</b> verify any proposed process with its internal labs and pilot tests.</p>
        </div>
        <div class="mission__col mission__col--it">
          <p><b>TFP ltd (TFP)</b> ha la missione di risolvere i problemi ambientali di qualsiasi cliente con la migliore soluzione di processo disponibile sul mercato, la più affidabile ed economica sia su CAPEX che su OPEX.</p>
          <p><b>Vogliamo</b> ottimizzare i vantaggi del cliente: energia, riciclaggio dell'acqua, recupero dei prodotti e riduzione delle emissioni.</p>
          <p><b>Verifichiamo</b> ogni processo proposto con i suoi laboratori interni e test pilota.</p>
        </div>
      </div>
    </article>
  </section>

  <section class="page page--right">
    <article class="provide">
      <h2 class="provide__title">We <b>Provide</b></h2>
      <ul class="provide__list">
        <li>Feasibility studies</li>
        <li>Pilot ttest</li>
        <li>Process design and guarantees<br>(over 240 plants successfully executed and<br>running)</li>
        <li>Basic and detailed engineering</li>
        <li>Key equipment support</li>
        <li>Construction and start-up supervision</li>
        <li>Operation and supervision expertise<br>(more than 20 years of internal expertise of<br>various biological and chemical reactions)</li>
      </ul>
    </article>

    <div class="gallery">
      <div class="photo photo--tank" role="img" aria-label="Photo of large cylindrical digester tanks with walkways"></div>
      <div class="photo photo--basin" role="img" aria-label="Photo of aeration basins at a treatment plant"></div>
      <div class="photo photo--screw" role="img" aria-label="Photo of a sludge tank with a screw conveyor"></div>
      <div class="photo photo--plant" role="img" aria-label="Photo of steel piping and process equipment"></div>
    </div>

    <div class="brand"><span class="brand__dot"></span>TFP Tarlo Fluid Power</div>
  </section>
</main>
</body>
</html>
```